SKYTHRESH (drone photo and video) and Photogrammetry Services (mapping and 3D modeling)

We need a business card design for a SKYTHRESH. Our businesses provides (drone) Aerial Photo and Video Captures. However we also provide Photogrammetry (which is 3D modeling and mapping). We greatly value unique points of view taken of landscapes and subjects with aerial photography and videography. 3D modeling and mapping is the other area of focus and have an incredibly broad scope of applications and imaginative creativity.

Target Market(s)

Based out of Northern Virginia and serving the greater Virginia and Maryland areas

Industry/Entity Type

Drone Photo and video and Photogrammetry Services (mapping and 3D modeling)

Contact Information for Business Card

3D Models, Maps and Photo/Video Production name: Marcus Lindqvist email: mrl@skythresh.us website: skythresh.us phone: 571-308-6943; please also include "Aerial Photo/Video and 3D Mapping/Modeling"

Requirements
Must have
• Please make this design vertical and double sided. The selection box is not letting me choose Double Sided but that is my wish. Incorporate uploaded LOGO and color scheme
Nice to have
• Preferably does not feel too crowded and balances not having an exaggerated amount of distracting detail
Should not have
• do not cram bullet points or text in long form

```html
<!DOCTYPE html>
<html lang="en">
<head>
<meta charset="utf-8">
<title>SKYTHRESH — Business Card</title>
<link href="https://fonts.googleapis.com/css2?family=Montserrat:wght@400;800&family=Roboto+Condensed:wght@700&display=swap" rel="stylesheet">
<style>
  :root {
    --bg: #2b2b2d;
    --card: #fbfbfb;
    --swoosh: #ebebec;
    --swoosh-deep: #dedee0;
    --ink: #222224;
    --ink-soft: #3a3a3c;
    --sun-yellow: #f6c23a;
    --sun-orange: #f4892f;
    --sun-red: #e8384f;
  }
  * { box-sizing: border-box; margin: 0; padding: 0; }
  html, body { width: 1200px; height: 960px; overflow: hidden; }
  body {
    background: var(--bg);
    display: flex;
    align-items: center;
    justify-content: center;
    gap: 80px;
    font-family: "Montserrat", sans-serif;
  }
  .card {
    position: relative;
    width: 380px;
    height: 665px;
    background: var(--card);
    overflow: hidden;
    box-shadow: 0 18px 40px rgba(0,0,0,0.45);
  }
  .card__swoosh {
    position: absolute;
    inset: 0;
    width: 100%;
    height: 100%;
  }
  .brand {
    position: absolute;
    left: 0;
    right: 0;
    display: flex;
    align-items: center;
    justify-content: center;
    gap: 12px;
  }
  .card--front .brand { top: 250px; }
  .card--back .brand { top: 170px; }
  .brand__dot {
    width: 34px;
    height: 34px;
    border-radius: 50%;
    background: var(--sun-orange);
    flex: none;
  }
  .brand__name {
    font-weight: 800;
    font-size: 34px;
    letter-spacing: 1px;
    color: var(--ink);
  }
  .rule {
    position: absolute;
    left: 34px;
    right: 34px;
    height: 2px;
    background: linear-gradient(90deg, var(--sun-yellow), var(--sun-orange) 45%, var(--sun-red));
  }
  .card--front .rule { top: 520px; }
  .card--back .rule { top: 560px; }
  .contact {
    position: absolute;
    left: 118px;
    top: 400px;
  }
  .contact__name {
    font-weight: 800;
    font-size: 15px;
    letter-spacing: 0.5px;
    color: var(--ink);
    margin-bottom: 10px;
  }
  .contact__list { list-style: none; }
  .contact__item {
    display: flex;
    align-items: center;
    gap: 8px;
    font-size: 13px;
    color: var(--ink-soft);
    line-height: 20px;
  }
  .contact__icon { width: 11px; height: 11px; fill: var(--ink); flex: none; }
  .tagline {
    position: absolute;
    left: 0;
    right: 0;
    top: 590px;
    text-align: center;
    font-family: "Roboto Condensed", sans-serif;
    font-weight: 700;
    font-size: 16.5px;
    color: var(--ink);
  }
</style>
</head>
<body>

  <section class="card card--front" aria-label="Card front">
    <svg class="card__swoosh" viewBox="0 0 380 665" aria-hidden="true">
      <path d="M0 60 L140 60 L380 190 L380 330 L0 120 Z" fill="var(--swoosh)"/>
      <circle cx="190" cy="270" r="120" fill="var(--swoosh-deep)" opacity="0.55"/>
      <circle cx="200" cy="270" r="112" fill="var(--card)"/>
    </svg>
    <div class="brand">
      <span class="brand__dot"></span>
      <span class="brand__name">SKYTHRESH</span>
    </div>
    <div class="rule"></div>
  </section>

  <section class="card card--back" aria-label="Card back">
    <svg class="card__swoosh" viewBox="0 0 380 665" aria-hidden="true">
      <path d="M0 70 L0 150 L90 200 L90 110 Z" fill="var(--swoosh)"/>
      <circle cx="180" cy="190" r="96" fill="var(--swoosh-deep)" opacity="0.5"/>
      <circle cx="190" cy="190" r="90" fill="var(--card)"/>
    </svg>
    <div class="brand">
      <span class="brand__dot"></span>
      <span class="brand__name">SKYTHRESH</span>
    </div>

    <div class="contact">
      <p class="contact__name">MARCUS LINDQVIST</p>
      <ul class="contact__list">
        <li class="contact__item">
          <svg class="contact__icon" viewBox="0 0 24 24" aria-hidden="true"><path d="M6.6 10.8a15 15 0 0 0 6.6 6.6l2.2-2.2a1 1 0 0 1 1-.25 11.4 11.4 0 0 0 3.6.57 1 1 0 0 1 1 1V20a1 1 0 0 1-1 1A17 17 0 0 1 3 4a1 1 0 0 1 1-1h3.5a1 1 0 0 1 1 1c0 1.25.2 2.45.57 3.57a1 1 0 0 1-.25 1z"/></svg>
          571-308-6943
        </li>
        <li class="contact__item">
          <svg class="contact__icon" viewBox="0 0 24 24" aria-hidden="true"><path d="M2 5h20v14H2z M2 5l10 8 10-8" /></svg>
          mrl@skythresh.us
        </li>
        <li class="contact__item">
          <svg class="contact__icon" viewBox="0 0 24 24" aria-hidden="true"><path d="M12 2a10 10 0 1 0 0 20 10 10 0 0 0 0-20zm6.9 6h-3a15.6 15.6 0 0 0-1.4-3.6A8 8 0 0 1 18.9 8zM12 4a14 14 0 0 1 1.9 4h-3.8A14 14 0 0 1 12 4zM4.3 14a8 8 0 0 1 0-4h3.4a16 16 0 0 0 0 4zm.8 2h3a15.6 15.6 0 0 0 1.4 3.6A8 8 0 0 1 5.1 16zm3-8h-3a8 8 0 0 1 4.4-3.6A15.6 15.6 0 0 0 8.1 8zM12 20a14 14 0 0 1-1.9-4h3.8A14 14 0 0 1 12 20zm2.3-6H9.7a14 14 0 0 1 0-4h4.6a14 14 0 0 1 0 4zm.2 5.6a15.6 15.6 0 0 0 1.4-3.6h3a8 8 0 0 1-4.4 3.6zm1.8-5.6a16 16 0 0 0 0-4h3.4a8 8 0 0 1 0 4z"/></svg>
          www.skythresh.us
        </li>
      </ul>
    </div>

    <div class="rule"></div>
    <p class="tagline">Aerial Photo/Video and 3D Mapping/Modeling</p>
  </section>

</body>
</html>
```